Brintell's Business Card

I need some designs for a new business card including the new logo attached. An old example of our business card is also attached to show all the data that should be included on the new design.
**I added some more examples someone had mocked up**

Contact Information for Business Card

Should include all info on other examples uploaded.

```html
<!DOCTYPE html>
<html lang="en">
<head>
<meta charset="utf-8">
<title>Brintell's Business Card</title>
<link href="https://fonts.googleapis.com/css2?family=Montserrat:wght@600;800&family=Lexend:wght@300;400&display=swap" rel="stylesheet">
<style>
  :root {
    --page: #ebebeb;
    --card-white: #f7f7f7;
    --brand-blue: #0a62ad;
    --brand-blue-light: #0b74bb;
    --brand-blue-dark: #06529a;
    --brand-red: #df1f26;
    --band-red: #d42f27;
    --band-red-light: #e2443a;
    --text-white: #ffffff;
  }
  * { margin: 0; padding: 0; box-sizing: border-box; }
  html, body {
    width: 1200px; height: 1200px; overflow: hidden;
    background: var(--page);
  }
  .card {
    position: absolute; left: 235px; width: 730px; height: 418px;
    overflow: hidden;
    box-shadow: 0 6px 18px rgba(0,0,0,0.18);
  }
  .card-front { top: 160px; background: linear-gradient(135deg, #ffffff, var(--card-white)); }
  .card-back { top: 631px; background: linear-gradient(120deg, var(--brand-blue-dark), var(--brand-blue-light)); }

  .brand-lockup { position: absolute; display: flex; align-items: center; gap: 12px; }
  .brand-dot { width: 30px; height: 30px; border-radius: 50%; background: var(--brand-red); }
  .brand-name {
    font-family: "Montserrat", sans-serif; font-weight: 600;
    line-height: 1; letter-spacing: 0.5px;
  }
  .card-front .brand-lockup { left: 53px; top: 72px; }
  .card-front .brand-name { font-size: 46px; color: var(--brand-blue); }

  .person-name {
    position: absolute; left: 53px; top: 212px;
    font-family: "Montserrat", sans-serif; font-weight: 800;
    font-size: 33px; color: var(--brand-red); letter-spacing: 0.3px;
  }
  .contact-line {
    position: absolute; left: 51px; display: flex; align-items: center; gap: 9px;
    font-family: "Lexend", sans-serif; font-weight: 300;
    font-size: 23px; color: var(--brand-blue);
  }
  .contact-phone { top: 257px; }
  .contact-email { top: 290px; }
  .contact-icon { width: 20px; height: 20px; fill: var(--brand-red); }

  .front-bands { position: absolute; left: 0; top: 361px; width: 730px; height: 57px; }
  .band-label {
    position: absolute; top: 361px; height: 57px; display: flex; align-items: center;
    font-family: "Lexend", sans-serif; font-weight: 300;
    font-size: 20px; color: var(--text-white); letter-spacing: 0.3px;
  }
  .label-licensed { left: 52px; }
  .label-family { left: 383px; }

  .back-bands { position: absolute; inset: 0; width: 730px; height: 418px; }
  .service-area, .call-line {
    position: absolute; left: 0; width: 730px; text-align: center;
    font-family: "Lexend", sans-serif; font-weight: 300; color: var(--text-white);
  }
  .service-area { top: 0; height: 66px; line-height: 68px; font-size: 24px; letter-spacing: 0.4px; }
  .call-line { top: 352px; height: 66px; line-height: 66px; font-size: 17px; letter-spacing: 0.3px; }
  .card-back .brand-lockup { left: 0; width: 730px; justify-content: center; top: 172px; gap: 16px; }
  .card-back .brand-dot { width: 40px; height: 40px; }
  .card-back .brand-name { font-size: 62px; color: var(--text-white); }
</style>
</head>
<body>
  <section class="card card-front">
    <div class="brand-lockup">
      <span class="brand-dot"></span>
      <span class="brand-name">BRINTELL'S</span>
    </div>

    <h1 class="person-name">DALE BRINTELL</h1>

    <div class="contact-line contact-phone">
      <svg class="contact-icon" viewBox="0 0 24 24" aria-hidden="true"><path d="M6.6 10.8a15.1 15.1 0 0 0 6.6 6.6l2.2-2.2c.3-.3.7-.4 1-.2 1.1.4 2.3.6 3.6.6.6 0 1 .4 1 1V20c0 .6-.4 1-1 1A17 17 0 0 1 3 4c0-.6.4-1 1-1h3.5c.6 0 1 .4 1 1 0 1.3.2 2.5.6 3.6.1.3 0 .7-.2 1z"/></svg>
      <span>555.014.2270</span>
    </div>
    <div class="contact-line contact-email">
      <svg class="contact-icon" viewBox="0 0 24 24" aria-hidden="true"><path d="M2 5h20v14H2z M2 5l10 7 10-7" fill="var(--brand-red)"/><path d="M2.5 6l9.5 6.6L21.5 6" fill="none" stroke="#fff" stroke-width="1.6"/></svg>
      <span>service@brintellhvac.net</span>
    </div>

    <svg class="front-bands" viewBox="0 0 730 57" aria-hidden="true">
      <defs>
        <linearGradient id="frontBlue" x1="0" x2="1">
          <stop offset="0" stop-color="var(--brand-blue-dark)"/>
          <stop offset="1" stop-color="var(--brand-blue-light)"/>
        </linearGradient>
      </defs>
      <path d="M0 0 H275 C300 0 315 8 330 22 L366 57 H0 Z" fill="url(#frontBlue)"/>
      <path d="M340 0 H730 V57 H375 L336 14 C331 8 333 0 340 0 Z" fill="var(--brand-red)"/>
    </svg>
    <span class="band-label label-licensed">LICENSED &amp; INSURED</span>
    <span class="band-label label-family">FAMILY OWNED &amp; OPERATED</span>
  </section>

  <section class="card card-back">
    <svg class="back-bands" viewBox="0 0 730 418" aria-hidden="true">
      <defs>
        <linearGradient id="backRed" x1="0" x2="1">
          <stop offset="0" stop-color="var(--band-red)"/>
          <stop offset="1" stop-color="var(--band-red-light)"/>
        </linearGradient>
      </defs>
      <path d="M0 0 H730 V66 H388 L365 89 L342 66 H0 Z" fill="url(#backRed)"/>
      <path d="M0 352 H342 L365 329 L388 352 H730 V418 H0 Z" fill="url(#backRed)"/>
    </svg>
    <p class="service-area">SERVES MAPLE FALLS, IA &amp; SURROUNDING AREAS</p>
    <div class="brand-lockup">
      <span class="brand-dot"></span>
      <span class="brand-name">BRINTELL'S</span>
    </div>
    <p class="call-line">CALL TODAY FOR ALL YOUR HVAC, REFRIGERATION &amp; PLUMBING NEEDS</p>
  </section>
</body>
</html>
```